letterhead design for a investing company*

Design an appealing business letterhead to match with our existing logo and attract new customers. Our customers are mainly corporate managers which are detail oriented and judge the company ability to perform a good service based on small details. A professional letterhead will give a good first impression.

Target Market(s)

New customers and business owners

Industry/Entity Type

Marketplace

Font styles to use
Sans Serif
Script

Requirements
Must have
• Must be a professional and elegant design that attracts interest from people who receives it

```html
<!DOCTYPE html>
<html lang="en">
<head>
<meta charset="utf-8">
<title>Brightwell Letterhead</title>
<link rel="stylesheet" href="https://fonts.googleapis.com/css2?family=Poppins:wght@300;400;600&display=swap">
<style>
  :root {
    --navy: #121d3d;
    --gold: #fdb913;
    --ink: #2a2a2a;
    --backdrop: #ececec;
    --paper: #ffffff;
    --rule: #9a9a9a;
  }
  * { margin: 0; padding: 0; box-sizing: border-box; }
  html, body {
    width: 960px; height: 1200px; overflow: hidden;
    background: var(--backdrop);
    font-family: "Poppins", sans-serif;
    color: var(--ink);
  }
  .letterhead {
    position: absolute; left: 53px; top: 0;
    width: 854px; height: 1200px;
    background: var(--paper);
    overflow: hidden;
  }
  .page-shapes { position: absolute; inset: 0; width: 100%; height: 100%; }
  .brand {
    position: absolute; left: 462px; top: 124px;
    display: flex; align-items: center; gap: 12px;
  }
  .brand-dot { width: 44px; height: 44px; border-radius: 50%; background: var(--gold); }
  .brand-name { font-weight: 600; font-size: 48px; line-height: 1; color: var(--navy); letter-spacing: -0.5px; }
  .salutation {
    position: absolute; left: 79px; top: 351px;
    font-size: 21px; font-weight: 400; color: #333;
  }
  .letter-body {
    position: absolute; left: 79px; top: 414px; width: 704px;
    font-size: 12.3px; line-height: 18.3px; font-weight: 300; color: #333;
  }
  .letter-body p { margin-bottom: 18.3px; }
  .closing {
    position: absolute; left: 79px; top: 801px;
    font-size: 12.3px; font-weight: 300; color: #333;
  }
  .signature {
    position: absolute; left: 79px; top: 845px; width: 112px; height: 65px;
    background: linear-gradient(90deg, #e4e4e4, #f1f1f1);
    border-radius: 4px;
  }
  .footer { position: absolute; left: 83px; top: 1117px; width: 521px; }
  .footer-address {
    font-size: 13.5px; font-weight: 400; color: #222;
    padding-bottom: 2px; border-bottom: 1px solid var(--rule);
  }
  .footer-contacts {
    display: flex; align-items: center; gap: 4px; margin-top: 4px;
    font-size: 13.5px; color: #222; white-space: nowrap;
  }
  .footer-contacts svg { width: 11px; height: 11px; fill: #222; flex: none; }
  .footer-contacts span { margin-right: 3px; }
</style>
</head>
<body>
<div class="letterhead">
  <svg class="page-shapes" viewBox="0 0 792 1113" preserveAspectRatio="none" aria-hidden="true">
    <path d="M0,0 H700 C470,30 210,150 0,306 Z" fill="var(--gold)"/>
    <path d="M0,0 H692 C455,25 195,135 0,281 Z" fill="var(--navy)"/>
    <path d="M792,1007 C720,1065 650,1098 568,1113 H792 Z" fill="var(--gold)"/>
    <path d="M792,1022 C728,1070 662,1100 586,1113 H792 Z" fill="var(--navy)"/>
  </svg>

  <div class="brand">
    <div class="brand-dot"></div>
    <div class="brand-name">Brightwell</div>
  </div>

  <p class="salutation">Dear Mr. Carter,</p>

  <div class="letter-body">
    <p>Lorem ipsum dolor sit amet, consectetur adipiscing elit. Donec orci purus, luctus vitae dignissim eu, iaculis sed purus. Vivamus faucibus, ipsum nec aliquet viverra, leo mauris condimentum ligula, sit amet sagittis enim ligula quis arcu. Nam egestas tortor id nisi porttitor mattis. In tortor ante, ultricies in suscipit a, tempus non massa. Vivamus et auctor mi. Fusce vel massa nulla. Phasellus nec eros mauris, et scelerisque orci.</p>
    <p>Donec malesuada orci vitae nulla accumsan porta a id massa. Quisque accumsan iaculis magna sit amet fringilla. Maecenas consequat, magna eget tincidunt semper, odio nibh rutrum mi, id feugiat ante nisi eu risus. Vestibulum nunc orci, rhoncus a placerat in, ultricies in mi. Cras mattis varius eros, vel fringilla nisi suscipit eget. Quisque scelerisque sagittis nulla at porttitor.</p>
    <p>Sed id augue vitae urna euismod commodo aliquet a quam. Pellentesque arcu velit, cursus et malesuada ut, consequat et diam. Nullam erat sem, rhoncus id ullamcorper vitae, rhoncus et arcu. In ultricies ultricies nulla, ut rutrum nisi iaculis at. Donec eu magna a metus ornare faucibus. Fusce aliquet faucibus ultricies. Morbi semper, est id tincidunt gravida, sem arcu adipiscing lacus, ac bibendum nulla leo eu purus. Quisque nec diam sed risus consectetur a ccumsan quis quis nibh. Vestibulum id purus lorem.</p>
    <p>It is a long established fact that a reader will be distracted by the readable content of a page when looking at its layout. The point of using Lorem Ipsum is that it has a more-or-less normal distribution of letters, as opposed to using 'Content here, content here', making it look like readable English. Many desktop publishing packages</p>
  </div>

  <p class="closing">Sincerely,</p>
  <div class="signature" role="img" aria-label="Handwritten signature of the sender"></div>

  <div class="footer">
    <p class="footer-address">Brightwell LLC 2140 Harbor View Road, Portland, Oregon 97201</p>
    <div class="footer-contacts">
      <svg viewBox="0 0 16 16"><path d="M3.6 1.2l2.3 2.6-1.2 2a9 9 0 0 0 5.5 5.5l2-1.2 2.6 2.3-1.3 2.4C7.8 14.6 1.4 8.2 1.2 2.5z"/></svg>
      <span>555-014-2288</span>
      <svg viewBox="0 0 16 16"><path d="M4 1h8v4H4zM1 6h14v6h-3v3H4v-3H1zm4 4v4h6v-4z"/></svg>
      <span>555-014-2290</span>
      <svg viewBox="0 0 16 16"><path d="M1 3h14v10H1zm1.5 1.2v.4L8 8.6l5.5-4v-.4z"/></svg>
      <span>hello@brightwell.co</span>
      <svg viewBox="0 0 16 16"><circle cx="8" cy="8" r="7"/></svg>
      <span>brightwell.co</span>
    </div>
  </div>
</div>
</body>
</html>
```